SkyVarro logo and website for a cloud solution provider in the UK market

Produce a logo with strong brand identity and a website themed similar to the log design.

The website is for a company called SkyVarro limited. SkyVarro specialises in migrating businesses from their on premise infrastructure to cloud services such as Deskwell365, Torvane and also Pelligrin Host Systems.

We offer migration and management services to allow customers to focus on their core business letting SkyVarro manage their business IT services and infratructure.

The design should leverage the Quillent partner information for the cost savings of migrating on premise solutions to the cloud. The website should also leverage Quillents content syndication to help with marketing materials and campaigns. the website links can be found here: https://setandrun.quillent-example.com

The website must be suitable for both desktop and mobile platforms including smartphones and tablets.

The design should communicate financial savings, confidence and user flexibility.

Reason: I need a website which will easy render on mobile devices which isn't too cluttered and has clear areas where I can insert Quillent syndicate banner content of sizes 180x150, 600x90 or 600x250. For details of Quillent syndicated content please see: http://setandrun.quillent-example.com

Target Market(s)

Small to medium companies who use on premise email, Filemesh, and web infrastructure who want to migrate their business safely to the cloud.

Industry/Entity Type

It Company

Logo Text

SkyVarro

Number of Pages Required

4 page

```html
<!DOCTYPE html>
<html lang="en">
<head>
<meta charset="utf-8">
<title>SkyVarro Ltd – Cloud Solutions</title>
<link rel="stylesheet" href="https://fonts.googleapis.com/css2?family=Open+Sans:wght@400;600;700&display=swap">
<style>
:root{
  --brand:#29a8e0;
  --brand-dark:#1b8cc0;
  --amber:#c7852f;
  --tan:#b98d5c;
  --ink:#4a4a4a;
  --muted:#8c8c8c;
  --soft:#eef0f2;
  --footer:#2e2e2e;
  --footer-bar:#222;
  --white:#fff;
}
*{box-sizing:border-box;margin:0;padding:0}
html,body{width:820px;height:1200px;overflow:hidden}
body{font-family:"Open Sans",Arial,sans-serif;color:var(--ink);background:var(--white);position:relative}
.page{position:relative;width:820px;height:1200px}

/* header */
.site-header{position:absolute;top:0;left:0;width:820px;height:77px;display:flex;align-items:center;justify-content:space-between;padding:0 60px 0 55px;background:var(--white)}
.brand{display:flex;align-items:center;gap:10px;color:var(--brand);font-weight:700;font-size:17px}
.brand-dot{width:30px;height:30px;border-radius:50%;background:var(--brand)}
.main-nav{display:flex;align-items:center;gap:34px;font-size:11px;font-weight:600;color:#555}
.main-nav .active{color:var(--brand);border-bottom:2px solid var(--brand);padding:4px 0}
.search-icon{width:14px;height:14px}

/* hero */
.hero{position:absolute;top:77px;left:0;width:820px;height:355px}
.hero svg{position:absolute;inset:0}
.hero-copy{position:absolute;left:90px;top:90px;width:230px;color:var(--white)}
.hero-title{font-size:38px;font-weight:700;letter-spacing:1px}
.hero-text{font-size:8.5px;line-height:1.6;margin-top:10px;opacity:.9}
.hero-button{display:inline-block;margin:16px 0 0 20px;border:1px solid var(--white);color:var(--white);font-size:9px;padding:7px 16px;letter-spacing:.5px}
.hero-dots{position:absolute;left:172px;top:332px;display:flex;gap:6px}
.hero-dots span{width:7px;height:7px;border-radius:50%;background:rgba(255,255,255,.5)}
.hero-dots span:first-child{background:var(--white)}

/* services */
.services{position:absolute;top:432px;left:0;width:820px;height:320px;text-align:center}
.section-title{color:var(--brand);font-size:20px;font-weight:600;letter-spacing:.5px}
.services .section-title{margin-top:32px}
.title-rule{width:40px;height:2px;background:var(--brand);margin:8px auto 0}
.services-intro{width:610px;margin:12px auto 0;font-size:8px;line-height:1.65;color:var(--muted)}
.service-list{display:flex;justify-content:center;gap:70px;margin-top:28px}
.service-card{width:170px}
.service-icon{width:74px;height:74px;border-radius:50%;margin:0 auto;display:flex;align-items:center;justify-content:center}
.service-icon.blue{background:var(--brand)}
.service-icon.amber{background:var(--amber)}
.service-icon.tan{background:var(--tan)}
.service-name{font-size:13px;margin-top:12px;color:#555}
.service-text{font-size:7.5px;line-height:1.6;color:var(--muted);margin-top:8px}
.service-link{display:inline-block;font-size:8px;color:var(--brand);margin-top:8px;border-bottom:1px solid var(--brand)}

/* news and testimonials */
.updates{position:absolute;top:752px;left:0;width:820px;height:286px;background:var(--soft);padding:22px 65px;display:flex;gap:40px}
.updates .section-title{font-size:15px;text-align:left}
.news{width:360px}
.news-item{display:flex;gap:14px;margin-top:16px}
.news-thumb{width:140px;height:90px;flex:none;background:linear-gradient(135deg,#3c8fc8,#1d4f7d)}
.news-thumb.alt{background:linear-gradient(135deg,#6b8aa6,#1f2d3c)}
.news-heading{font-size:9px;color:var(--amber)}
.news-date{font-size:8px;color:var(--brand);margin-top:4px}
.news-text{font-size:7.5px;line-height:1.6;color:var(--muted);margin-top:6px}
.testimonials{width:355px}
.quote-box{background:var(--white);margin-top:16px;padding:18px 20px;font-size:8px;line-height:1.7;color:var(--muted);position:relative}
.quote-box::after{content:"";position:absolute;left:40px;bottom:-10px;border:10px solid transparent;border-bottom:0;border-top-color:var(--white)}
.client{display:flex;align-items:center;gap:14px;margin-top:22px;padding-left:22px}
.client-photo{width:48px;height:48px;border-radius:50%;background:linear-gradient(135deg,#8a6a52,#3d2d24)}
.client-name{font-size:9px;color:var(--muted)}

/* footer */
.site-footer{position:absolute;top:1038px;left:0;width:820px;height:137px;background:var(--footer);color:#cfcfcf;display:flex;padding:18px 0 0 80px}
.footer-col{font-size:8px}
.footer-title{font-size:11px;font-weight:600;color:var(--white);letter-spacing:.4px;margin-bottom:10px}
.newsletter{width:290px}
.field{width:165px;height:20px;background:#fff;margin-bottom:7px;color:#555;font-size:7.5px;padding:5px 8px}
.signup-button{width:165px;height:20px;background:var(--brand);color:var(--white);font-size:7.5px;text-align:center;line-height:20px}
.contact{width:200px;margin-left:30px}
.contact p{margin-bottom:7px;line-height:1.5}
.contact-line{display:flex;align-items:center;gap:8px}
.social{width:160px}
.social li{list-style:none;display:flex;align-items:center;gap:8px;margin-bottom:6px}
.social-dot{width:7px;height:7px;border-radius:50%;background:#cfcfcf}
.footer-bar{position:absolute;top:1175px;left:0;width:820px;height:25px;background:var(--footer-bar);color:#999;font-size:7px;text-align:center;line-height:25px}
.to-top{position:absolute;right:18px;top:0;color:#999}
</style>
</head>
<body>
<div class="page">

  <header class="site-header">
    <div class="brand"><span class="brand-dot"></span>SkyVarro LTD</div>
    <nav class="main-nav">
      <span class="active">HOME</span>
      <span>ABOUT US</span>
      <span>SERVICES</span>
      <span>BLOG</span>
      <span>CONTACT US</span>
      <svg class="search-icon" viewBox="0 0 14 14"><circle cx="6" cy="6" r="4" fill="none" stroke="#c7852f" stroke-width="1.6"/><line x1="9" y1="9" x2="13" y2="13" stroke="#c7852f" stroke-width="1.6"/></svg>
    </nav>
  </header>

  <section class="hero">
    <svg width="820" height="355" viewBox="0 0 820 355">
      <defs>
        <linearGradient id="sky" x1="0" y1="0" x2="0" y2="1">
          <stop offset="0" stop-color="#5aa9dc"/>
          <stop offset=".55" stop-color="#9cc8e8"/>
          <stop offset=".7" stop-color="#7c8c9a"/>
          <stop offset="1" stop-color="#2f6f9c"/>
        </linearGradient>
      </defs>
      <rect width="820" height="355" fill="url(#sky)" role="img" aria-label="Photo of a city skyline across the water"/>
      <path d="M0 0 H420 C360 90 360 250 440 355 H0 Z" fill="#29a8e0"/>
      <path d="M420 0 C360 90 360 250 440 355" fill="none" stroke="#fff" stroke-width="4"/>
    </svg>
    <div class="hero-copy">
      <h1 class="hero-title">WELCOME</h1>
      <p class="hero-text">We move your mail, files and sites to the cloud so your team can focus on growth while we look after the IT.</p>
      <span class="hero-button">READ MORE</span>
    </div>
    <div class="hero-dots"><span></span><span></span><span></span></div>
  </section>

  <section class="services">
    <h2 class="section-title">OUR SERVICES</h2>
    <div class="title-rule"></div>
    <p class="services-intro">From planning to daily support, we migrate small and medium businesses from on premise servers to secure cloud platforms. Lower running costs, fewer surprises and the freedom to work from anywhere, with a UK team that knows your setup.</p>
    <div class="service-list">
      <article class="service-card">
        <div class="service-icon blue">
          <svg width="36" height="24" viewBox="0 0 36 24"><path d="M9 22 A7 7 0 0 1 9 8 A10 10 0 0 1 27 7 A7.5 7.5 0 0 1 28 22 Z" fill="#fff"/></svg>
        </div>
        <h3 class="service-name">Deskwell365</h3>
        <p class="service-text">Move email, calendars and documents into Deskwell365 with zero downtime and a clear plan for every user.</p>
        <span class="service-link">CLICK HERE »</span>
      </article>
      <article class="service-card">
        <div class="service-icon amber">
          <svg width="26" height="30" viewBox="0 0 26 30"><path d="M3 1 H17 L23 7 V29 H3 Z" fill="#fff"/><path d="M8 13 H18 M8 18 H18 M8 23 H15" stroke="#c7852f" stroke-width="2"/></svg>
        </div>
        <h3 class="service-name">Torvane</h3>
        <p class="service-text">Run servers, backups and apps on Torvane with flexible capacity that grows or shrinks as you need it.</p>
        <span class="service-link">CLICK HERE »</span>
      </article>
      <article class="service-card">
        <div class="service-icon tan">
          <svg width="32" height="32" viewBox="0 0 32 32"><g fill="#fff"><circle cx="16" cy="16" r="9"/><rect x="14" y="2" width="4" height="28"/><rect x="2" y="14" width="28" height="4"/><rect x="14" y="2" width="4" height="28" transform="rotate(45 16 16)"/><rect x="14" y="2" width="4" height="28" transform="rotate(-45 16 16)"/></g><circle cx="16" cy="16" r="4" fill="#b98d5c"/></svg>
        </div>
        <h3 class="service-name">Pelligrin Host Systems</h3>
        <p class="service-text">Host websites and data on Pelligrin Host Systems with managed security and predictable monthly pricing.</p>
        <span class="service-link">CLICK HERE »</span>
      </article>
    </div>
  </section>

  <section class="updates">
    <div class="news">
      <h2 class="section-title">OUR NEWS</h2>
      <article class="news-item">
        <div class="news-thumb" role="img" aria-label="Photo of a data centre"></div>
        <div>
          <h3 class="news-heading">Cutting server costs in the cloud</h3>
          <p class="news-date">03 - SEP - 2015</p>
          <p class="news-text">A short look at how small firms lower yearly spend by retiring old hardware.</p>
        </div>
      </article>
      <article class="news-item">
        <div class="news-thumb alt" role="img" aria-label="Photo of a laptop at work"></div>
        <div>
          <h3 class="news-heading">Planning a safe Filemesh move</h3>
          <p class="news-date">03 - SEP - 2015</p>
          <p class="news-text">Steps we follow to keep files, rights and links intact during migration.</p>
        </div>
      </article>
    </div>
    <div class="testimonials">
      <h2 class="section-title">TESTIMONIALS</h2>
      <blockquote class="quote-box">SkyVarro moved our whole office to the cloud over one weekend. Monday morning everyone logged in as normal, and our IT bills have dropped every month since then.</blockquote>
      <div class="client">
        <div class="client-photo" role="img" aria-label="Portrait photo of the client"></div>
        <p class="client-name">Dana Rowe - IT Manager</p>
      </div>
    </div>
  </section>

  <footer class="site-footer">
    <div class="footer-col newsletter">
      <h4 class="footer-title">SIGN UP FOR NEWSLETTER</h4>
      <div class="field">Enter Name</div>
      <div class="field">Email</div>
      <div class="signup-button">SIGN UP NOW</div>
    </div>
    <div class="footer-col contact">
      <h4 class="footer-title">CONTACT US</h4>
      <p>Get in touch to plan your move to the cloud.</p>
      <p class="contact-line"><svg width="9" height="9" viewBox="0 0 10 10"><path d="M2 1 L4 1 L5 3 L4 4 Q5 6 6 6 L7 5 L9 6 L9 8 Q8 9 7 9 Q1 8 1 2 Q1 1 2 1 Z" fill="#cfcfcf"/></svg>+44 20 7946 0381</p>
      <p class="contact-line"><svg width="9" height="9" viewBox="0 0 10 10"><rect x="1" y="2" width="8" height="6" fill="none" stroke="#cfcfcf"/><path d="M1 2 L5 5 L9 2" fill="none" stroke="#cfcfcf"/></svg>www.skyvarro.co.uk</p>
    </div>
    <div class="footer-col social">
      <h4 class="footer-title">SOCIAL MEDIA</h4>
      <ul>
        <li><span class="social-dot"></span>Friendloop</li>
        <li><span class="social-dot"></span>Chirpline</li>
        <li><span class="social-dot"></span>Circlepost</li>
        <li><span class="social-dot"></span>Viewstream</li>
      </ul>
    </div>
  </footer>
  <div class="footer-bar">© 2015 SKYVARRO LTD. RIGHTS RESERVED<span class="to-top">⌃</span></div>

</div>
</body>
</html>
```